Harlow Creek Church Invite Card

We are a vibrant multigenerational church outside of Raleigh, NC and are wanting a 'church invite card' that we can encourage our members to carry with them so that they can invite their friends to church.

These cards should have a modern feel (see http://zentravio.com/neat-card-ideas/ for the feel we are going for), match the branding of our website (www.harlowcreek.org) and include the following information on the back:

Service Times: Sunday @ 8:30 AM and 11:00 AM (Main Focus)
Website: www.harlowcreek.org (Main Focus)
Social Media: (You can simply use the icons for these if desired)
www.plazebook.example/harlowcreekchurch
www.snapgrove.example/harlowcreekchurch
www.vidstream.example/harlowcreekyouth
Address: 4827 Marlow Avenue Wendell, NC 27500 (Not a main focus)
Phone: (919) 555-0182 (Not a main focus)

The front should simply say 'We look forward to meeting you!'

Logos: Attached you will find the necessary logos for this project.

Fonts and Colors: Here are the specific colors (See HCC_Website_Color_Palette.pdf) and fonts that are used on our website.
Pacifico
Helvetica
Open Sans Regular

Target Market(s)

Friends of our congregation

Industry/Entity Type

Church

Contact Information for Business Card

We will likely print through Quillby Printworks. The details of what they need can be found here: http://www.quillbyprint.example/products/business-card

Font styles to use
Other font styles liked:
• Pacifico, Helvetica, Open Sans Regular, Bebas Nue

Colors
0592cd
34a7d8
85cae6
cee9f5
0455a3
3176b5
85acd3
cfdfed

Requirements
Must have
• Sleek, eye catching design
Nice to have
• Rounded Corners, Our social media sites (PB, Snapg and VidStream)

```html
<!DOCTYPE html>
<html lang="en">
<head>
<meta charset="utf-8">
<title>Harlow Creek Church Invite Card</title>
<link rel="stylesheet" href="https://fonts.googleapis.com/css2?family=Open+Sans:wght@400;600;700;800&display=swap">
<style>
  :root {
    --backdrop: #d9d6d3;
    --card: #111213;
    --ink: #ffffff;
    --ink-soft: #d8d8d8;
    --brand-blue: #0592cd;
    --brand-deep: #3176b5;
    --rule: #8a8a8a;
  }
  * { margin: 0; padding: 0; box-sizing: border-box; }
  html, body { width: 1200px; height: 814px; overflow: hidden; }
  body {
    background: var(--backdrop);
    font-family: "Open Sans", Arial, sans-serif;
    position: relative;
  }
  .card {
    position: absolute;
    top: 257px;
    width: 525px;
    height: 300px;
    background: var(--card);
    border-radius: 10px;
    color: var(--ink);
    box-shadow: 0 8px 24px rgba(0,0,0,0.25);
  }
  .card--back { left: 50px; }
  .card--front { left: 625px; }

  .brand-name {
    font-weight: 800;
    color: var(--ink);
    letter-spacing: 0.5px;
    line-height: 1.1;
  }

  /* Back side */
  .card--back .brand-name {
    position: absolute;
    left: 40px;
    top: 160px;
    font-size: 26px;
    width: 230px;
  }
  .divider {
    position: absolute;
    left: 292px;
    top: 60px;
    width: 1px;
    height: 180px;
    background: var(--rule);
  }
  .contact {
    position: absolute;
    left: 316px;
    top: 70px;
    font-size: 14px;
    line-height: 1.35;
    color: var(--ink-soft);
    list-style: none;
  }
  .contact__address { margin-bottom: 4px; }
  .contact__item { display: flex; align-items: center; gap: 8px; }
  .contact__icon { width: 12px; height: 12px; flex: none; }
  .contact__mark {
    width: 11px; height: 11px; flex: none;
    background: var(--brand-deep);
    border-radius: 2px;
  }

  /* Front side */
  .card--front { text-align: center; }
  .card--front .brand-name {
    position: absolute;
    left: 0; right: 0;
    top: 70px;
    font-size: 32px;
  }
  .invite {
    position: absolute;
    left: 0; right: 0;
    top: 140px;
  }
  .invite__label {
    color: var(--brand-blue);
    font-weight: 700;
    font-size: 15px;
    letter-spacing: 0.3px;
  }
  .invite__times {
    font-weight: 700;
    font-size: 16px;
  }
  .invite__site {
    color: var(--brand-blue);
    font-weight: 600;
    font-size: 15px;
    letter-spacing: 0.4px;
    margin-top: 2px;
  }
  .invite__welcome {
    font-size: 14px;
    color: var(--ink-soft);
    margin-top: 8px;
  }
</style>
</head>
<body>
  <section class="card card--back" aria-label="Card back">
    <div class="brand-name">Harlow Creek Church</div>
    <div class="divider"></div>
    <ul class="contact">
      <li class="contact__address">4827 Marlow<br>Avenue Fenbrook<br>NC 27500</li>
      <li class="contact__item">
        <svg class="contact__icon" viewBox="0 0 24 24" aria-hidden="true"><path fill="#3176b5" d="M6.6 10.8a15.1 15.1 0 0 0 6.6 6.6l2.2-2.2c.3-.3.7-.4 1-.2 1.1.4 2.3.6 3.6.6.6 0 1 .4 1 1V20c0 .6-.4 1-1 1A17 17 0 0 1 3 4c0-.6.4-1 1-1h3.5c.6 0 1 .4 1 1 0 1.3.2 2.5.6 3.6.1.3 0 .7-.2 1z"/></svg>
        (919) 555-0182
      </li>
      <li class="contact__item"><span class="contact__mark"></span>harlowcreekchurch</li>
      <li class="contact__item"><span class="contact__mark"></span>harlowcreekchurch</li>
      <li class="contact__item"><span class="contact__mark"></span>harlowcreekchurch</li>
    </ul>
  </section>

  <section class="card card--front" aria-label="Card front">
    <div class="brand-name">Harlow Creek Church</div>
    <div class="invite">
      <p class="invite__label">SERVICE TIMES:</p>
      <p class="invite__times">Sunday @ 8:30 AM and 11:00 AM</p>
      <p class="invite__site">WWW.HARLOWCREEK.ORG</p>
      <p class="invite__welcome">We look forward to meeting you!</p>
    </div>
  </section>
</body>
</html>
```